Flyer design for established pet care company
The Meadowkeepers
Professional pet care for the discerning pet lover
I'm looking to create an eyecatching A5 flyer to help get my business back out there and in front of the ever increasing competition. My website www.the-meadowkeepers-zq.co.uk shows you what I'm all about.
Animals
Pet lovers
I would like to see designs with and without the logo if possible.
Selection of photos for use with flyer

```html
<!DOCTYPE html>
<html lang="en">
<head>
<meta charset="utf-8">
<title>The Meadowkeepers – A5 Flyer</title>
<link href="https://fonts.googleapis.com/css2?family=PT+Sans:ital,wght@0,400;0,700;1,400;1,700&display=swap" rel="stylesheet">
<style>
  :root{
    --backdrop:#9a9a9a;
    --purple:#5a1f6e;
    --purple-deep:#3f1150;
    --green:#1f5a2a;
    --green-deep:#123d1b;
    --yellow:#f6e21a;
    --white:#ffffff;
    --grass:#6f9a3a;
  }
  *{box-sizing:border-box;margin:0;padding:0}
  html,body{width:1200px;height:901px;overflow:hidden}
  body{background:var(--backdrop);font-family:"PT Sans",Arial,sans-serif;position:relative}
  .page{position:absolute;top:97px;width:483px;height:773px;overflow:hidden;box-shadow:0 4px 14px rgba(0,0,0,.35)}
  .page--front{left:97px}
  .page--back{left:601px;background:var(--purple)}
  .abs{position:absolute}
  .bullet{flex:none;width:9px;height:9px;border-radius:50%;background:var(--yellow);margin-top:5px}

  /* front */
  .front-photo{left:0;top:0;width:483px;height:650px;background:linear-gradient(180deg,#c9dcc0 0%,#9cbf7a 35%,var(--grass) 65%,#4d7a2a 100%)}
  .brand{left:22px;top:100px;color:var(--yellow);font-weight:700;font-size:34px;line-height:1;display:flex;align-items:center;gap:8px}
  .brand__dot{width:13px;height:13px;border-radius:50%;background:var(--yellow)}
  .brand-tag{left:60px;top:146px;color:var(--white);font-style:italic;font-weight:700;font-size:14px;line-height:1.15;width:200px;text-align:right}
  .front-base{left:0;top:560px;width:483px;height:213px}
  .services{left:30px;top:588px;width:150px;height:178px;background:var(--purple);padding:16px 12px}
  .services li{list-style:none;color:var(--yellow);font-weight:700;font-style:italic;font-size:16px;line-height:1.22;display:flex;gap:7px;margin-bottom:2px}
  .contact{color:var(--white);font-style:italic;text-align:right}
  .contact__note{font-size:14px;line-height:1.2}
  .contact__line{color:var(--yellow);font-weight:700;font-size:24px;line-height:1.08;font-style:normal}
  .front-contact{right:18px;top:640px;width:260px}

  /* back */
  .intro{left:0;top:20px;width:483px;text-align:center;color:var(--white);font-size:21px;line-height:1.2}
  .headline{left:0;top:84px;width:483px;text-align:center;color:var(--yellow);font-weight:700;font-style:italic;font-size:38px;line-height:1.2}
  .back-photo{left:34px;top:140px;width:204px;height:206px;background:linear-gradient(160deg,#f1e6d6 0%,#d9b68f 50%,#8a5d3b 100%);border:3px solid var(--white)}
  .prices{left:250px;top:140px;width:225px;color:var(--white);font-size:11.5px;line-height:1.2}
  .prices h3{color:var(--yellow);font-size:16px;line-height:1.05;text-transform:uppercase}
  .prices h4{color:var(--yellow);font-size:13px;margin-top:3px}
  .prices .amount{font-weight:700;font-size:14px;color:var(--white)}
  .prices .sec{margin-top:6px}
  .charges{left:0;top:355px;width:483px;height:24px;background:var(--yellow);color:var(--purple);font-weight:700;font-style:italic;font-size:15px;line-height:24px;text-align:center}
  .rates{left:20px;top:385px;width:443px;color:var(--white);font-size:8.5px;line-height:1.3}
  .about{left:0;top:418px;width:483px;padding:0 18px;color:var(--white)}
  .about p{font-size:11px;line-height:1.3;font-weight:700;color:var(--yellow)}
  .about__cols{display:flex;gap:14px;margin-top:6px}
  .about__cols ul{flex:1}
  .about__cols li{list-style:none;font-size:9.5px;line-height:1.25;display:flex;gap:5px;margin-bottom:6px}
  .about__cols .bullet{width:8px;height:8px;margin-top:2px}
  .back-base{left:0;top:590px;width:483px;height:183px}
  .back-brand{left:20px;top:648px;color:var(--yellow);font-weight:700;font-size:24px;line-height:1;display:flex;align-items:center;gap:6px}
  .back-brand .brand__dot{width:10px;height:10px}
  .back-tag{left:30px;top:678px;width:200px;color:var(--white);font-size:10px;font-style:italic;font-weight:700;text-align:center}
  .back-contact{right:14px;top:650px;width:215px}
  .back-contact .contact__note{font-size:11px}
  .back-contact .contact__line{font-size:21px}
</style>
</head>
<body>

<section class="page page--front">
  <div class="abs front-photo" role="img" aria-label="Photo of a woman walking several dogs on a sunny lawn"></div>
  <div class="abs brand"><span>The Meadowkeepers</span><span class="brand__dot"></span></div>
  <p class="abs brand-tag">Professional pet care for the discerning pet lovers</p>

  <svg class="abs front-base" viewBox="0 0 483 213" preserveAspectRatio="none" aria-hidden="true">
    <path d="M0 50 C150 10 330 0 483 14 L483 213 L0 213 Z" fill="var(--yellow)"/>
    <path d="M0 62 C150 24 330 14 483 28 L483 213 L0 213 Z" fill="var(--green)"/>
    <path d="M0 160 C200 140 360 150 483 130 L483 213 L0 213 Z" fill="var(--green-deep)" opacity=".5"/>
  </svg>

  <ul class="abs services">
    <li><span class="bullet"></span>Dog Walking</li>
    <li><span class="bullet"></span>Cat care</li>
    <li><span class="bullet"></span>Microchipping</li>
    <li><span class="bullet"></span>BTEC Qualifications</li>
    <li><span class="bullet"></span>ACC Qualifications</li>
  </ul>

  <div class="abs contact front-contact">
    <p class="contact__note">Please feel free to contact us with any questions you may have. We can be reached by several different means:</p>
    <p class="contact__line" style="margin-top:10px">MOB.: 07700 900417</p>
    <p class="contact__line">TEL.: 01632 960884</p>
  </div>
</section>

<section class="page page--back">
  <p class="abs intro">As well as client recommendations<br>we are recommended by</p>
  <h2 class="abs headline">Vets and Dog Groomers.</h2>

  <div class="abs back-photo" role="img" aria-label="Photo of a smiling woman holding a small long-haired dog"></div>

  <div class="abs prices">
    <h3>Pet sitting/ day care<br>visits costs</h3>
    <h4>Cats &amp; Small Furries</h4>
    <p><span class="amount">£10.00</span> per visit<br>for all animals in household</p>
    <div class="sec">
      <h3>Dog walking costs</h3>
      <p><span class="amount">£10.00 + £5.00</span> per<br>additional dog for 60 minutes</p>
    </div>
    <div class="sec">
      <h3>Additional services</h3>
      <h4 style="margin-top:1px">Microchipping</h4>
      <p class="amount">£16.00</p>
    </div>
  </div>

  <p class="abs charges">Charges for Dog Walking apply from Monday to Friday</p>
  <p class="abs rates">Weekend visits are charged at 1.5x and Bank Holiday visits at 2x. Christmas Day and New Year's Day visits are charged at 2.5x. Charges for Pet Sitting and Day Care apply Monday to Sunday.</p>

  <div class="abs about">
    <p>My name is Harriet Lowe and I've been involved in working with animals for 22 years. I also have a few of my own who keep me well and truly on my toes! My furry family consists of:</p>
    <div class="about__cols">
      <ul>
        <li><span class="bullet"></span>Jasper my tri-colour Collie, an excellent teaching dog for our Dog to Dog Socialisation Programme</li>
        <li><span class="bullet"></span>Four cats * Prudence an Oriental Longhair, Eric a Balinese, Mowser an Egyptian Mau and Paddy a Siamese cross. *It is with great sadness that I write that Eric had to</li>
      </ul>
      <ul>
        <li><span class="bullet"></span>be put to sleep on 19 August just 4 days shy of his 6th birthday due to chronic kidney failure*</li>
        <li><span class="bullet"></span>Eight chickens from a local hen rescue</li>
        <li><span class="bullet"></span>A 1 year old African Grey Parrot called Pennie</li>
      </ul>
    </div>
  </div>

  <svg class="abs back-base" viewBox="0 0 483 183" preserveAspectRatio="none" aria-hidden="true">
    <path d="M0 30 C150 0 330 -4 483 10 L483 183 L0 183 Z" fill="var(--yellow)"/>
    <path d="M0 40 C150 12 330 8 483 22 L483 183 L0 183 Z" fill="var(--green)"/>
  </svg>

  <div class="abs back-brand"><span>The Meadowkeepers</span><span class="brand__dot"></span></div>
  <p class="abs back-tag">Professional pet care for the discerning pet lovers</p>

  <div class="abs contact back-contact">
    <p class="contact__note">Please feel free to contact us with any questions you may have.</p>
    <p class="contact__line" style="margin-top:6px">MOB.: 07700 900417</p>
    <p class="contact__line">TEL.: 01632 960884</p>
  </div>
</section>

</body>
</html>
```